Produktetikett für Mikronährstoffe
Wir sind sehr zufrieden und schätzen die schnelle Umsetzung von Änderungswünschen. Herzlichen Dank an Wilmaru
Zielgruppe
Herstellung und Vertrieb von Desinfektionsmitteln und jetz neu Mikronährstoffe. Und darum geht es. Wir möchten ein Etikett gestalten lassen das modern ist und trotzdem unsere Firmenfarben und unser Logo (evtl. stilisiert) enthält. Wahrscheinlich werden wir eine braune Flasche (ähnl. Apothekerflaschen) wählen.
Aufgabenstellung
Produktetikett für Mikronährstoffe (im Nahrungsergänzungsbereich) Die Ausführung der Flasche ist noch nicht bekannnt, jedoch schwebt uns eine braune oder dunkelgrüne Flasche vor. Auch gibt es noch keinen Namen für das Produkt.

```html
<!DOCTYPE html>
<html lang="de">
<head>
<meta charset="utf-8">
<title>Valmorin Mikronährstoffe – Produktetikett</title>
<link rel="stylesheet" href="https://fonts.googleapis.com/css2?family=Montserrat:wght@500;700;800&family=Nunito:wght@800;900&display=swap">
<style>
  :root {
    --backdrop: #a7a7a7;
    --paper: #ffffff;
    --brand-blue: #00a5c8;
    --brand-green: #8cc63f;
    --leaf-green: #97c13c;
    --lime: #cfdc2c;
    --text-white: #ffffff;
  }
  * { margin: 0; padding: 0; box-sizing: border-box; }
  html, body { width: 764px; height: 1200px; overflow: hidden; }
  body {
    background: var(--backdrop);
    position: relative;
    font-family: "Nunito", "Montserrat", sans-serif;
  }
  .label {
    position: absolute;
    left: 32px;
    top: 329px;
    width: 700px;
    height: 542px;
    background: var(--paper);
    overflow: hidden;
    box-shadow: 0 6px 14px rgba(0,0,0,0.25);
  }
  .label-art {
    position: absolute;
    inset: 0;
    width: 700px;
    height: 542px;
  }
  .brand-name {
    position: absolute;
    top: 40px;
    left: 0;
    width: 672px;
    text-align: center;
    font-family: "Montserrat", sans-serif;
    font-weight: 500;
    font-size: 40px;
    letter-spacing: 1px;
    color: var(--brand-blue);
  }
  .product-title {
    position: absolute;
    top: 166px;
    left: 0;
    width: 700px;
    text-align: center;
    font-family: "Nunito", sans-serif;
    font-weight: 900;
    font-size: 72px;
    letter-spacing: -1px;
    line-height: 1;
    color: var(--brand-blue);
  }
  .product-category {
    position: absolute;
    top: 250px;
    left: 136px;
    width: 480px;
    text-align: center;
    font-family: "Nunito", sans-serif;
    font-weight: 900;
    font-size: 31px;
    line-height: 1;
    color: var(--brand-green);
  }
  .ingredient-list {
    position: absolute;
    top: 333px;
    left: 70px;
    list-style: none;
  }
  .ingredient-list li {
    position: relative;
    padding-left: 29px;
    height: 28.4px;
    font-weight: 900;
    font-size: 22px;
    line-height: 28px;
    color: var(--text-white);
  }
  .ingredient-list li::before {
    content: "";
    position: absolute;
    left: 4px;
    top: 10px;
    width: 10px;
    height: 10px;
    border-radius: 50%;
    background: var(--text-white);
  }
  .badge {
    position: absolute;
    width: 100px;
    height: 100px;
    border-radius: 50%;
    background: var(--paper);
    box-shadow: 0 2px 6px rgba(0,0,0,0.2);
    color: var(--brand-blue);
    text-align: center;
    font-weight: 900;
  }
  .badge-count { left: 383px; top: 311px; }
  .badge-omega { left: 323px; top: 386px; }
  .badge-count .big { display: block; font-size: 44px; line-height: 1; margin-top: 18px; }
  .badge-count .small { display: block; font-size: 13px; line-height: 1; }
  .badge-omega .small { display: block; font-size: 15px; line-height: 1; margin-top: 18px; }
  .badge-omega .big { display: block; font-size: 44px; line-height: 1; }
  .net-weight {
    position: absolute;
    top: 496px;
    left: 183px;
    width: 140px;
    text-align: center;
    font-weight: 800;
    font-size: 13.5px;
    color: var(--text-white);
  }
</style>
</head>
<body>
  <section class="label">
    <svg class="label-art" viewBox="0 0 1158 897" preserveAspectRatio="none" aria-hidden="true">
      <defs>
        <linearGradient id="wave-green" x1="0" y1="0" x2="0" y2="1">
          <stop offset="0" stop-color="var(--lime)"/>
          <stop offset="0.35" stop-color="var(--leaf-green)"/>
          <stop offset="1" stop-color="var(--leaf-green)"/>
        </linearGradient>
        <linearGradient id="produce" x1="0" y1="0" x2="1" y2="1">
          <stop offset="0" stop-color="#e8541f"/>
          <stop offset="0.35" stop-color="#f4a21c"/>
          <stop offset="0.6" stop-color="#5a4a7c"/>
          <stop offset="0.85" stop-color="#c9d94a"/>
          <stop offset="1" stop-color="#d8405a"/>
        </linearGradient>
      </defs>
      <path class="green-wave" d="M0 632 C 90 540 220 498 320 500 C 470 504 650 532 852 540 L 860 897 L 0 897 Z" fill="url(#wave-green)"/>
      <path class="blue-swoosh" d="M0 800 C 200 810 420 790 540 742 L 545 760 C 420 830 200 860 0 868 Z" fill="var(--brand-blue)"/>
    </svg>
    <svg class="label-art" viewBox="0 0 1158 897" preserveAspectRatio="none" role="img" aria-label="Foto mit frischem Obst und Gemüse: Paprika, Trauben, Äpfel, Limetten und Orangen">
      <path d="M862 532 C 960 500 1060 490 1158 488 L 1158 897 L 612 897 Z" fill="url(#produce)"/>
    </svg>

    <div class="brand-name">Valmorin</div>
    <h1 class="product-title">Mikronährstoffe</h1>
    <p class="product-category">Nahrungsergänzungsmittel</p>

    <ul class="ingredient-list">
      <li>Vitamine</li>
      <li>Mineralstoffe</li>
      <li>Spurenelemente</li>
      <li>Pflanzenstoffe</li>
    </ul>

    <div class="badge badge-count"><span class="big">60</span><span class="small">Capsules</span></div>
    <div class="badge badge-omega"><span class="small">Omega</span><span class="big">3</span></div>

    <p class="net-weight">Net Weight 65 g</p>
  </section>
</body>
</html>
```